Tot Petal Product Label for Tear-Free Head-to-Toe Wash

Need a bottle label design for a new line of natural products targeting infants and children. Products are Pediatrician-developed and paraben-free, sulfate-free, fragrance-free, and cruelty-free. Design should be clean and have a high-end feel to it. Will need other product labels in Tot Petal line designed as well in upcoming projects.

Target Market(s)

Newborn to young elementary age children and their parents

Industry/Entity Type

Cosmetics/Beauty

Font styles to use
Other font styles liked:
• Brand fonts are Jost and Sonorous

Colors

Designer to choose colors to be used in the design.

Requirements
Must have
• Tot Petal logo, Pediatrician Developed logo, and a clean high-end feel to it. The label must fit the specialty bottle we will be using (label measurements and diagram will be provided) for the front and back of bottle only (NOT the side labels). It must include our list of ingredients (will provide once designer selected).
Nice to have
• Should stand out on the shelf of other baby products due to it's clean simplicity and high-end feel
Should not have
• too much of a "kiddie" feel to it (targeting the parents not the kids)

```html
<!DOCTYPE html>
<html lang="en">
<head>
<meta charset="UTF-8">
<title>Tot Petal – Tear-Free Head-to-Toe Wash Label</title>
<link rel="stylesheet" href="https://fonts.googleapis.com/css2?family=Fredoka:wght@500;600;700&family=Jost:wght@400;500;600&display=swap">
<style>
  :root {
    --page: #ffffff;
    --label-top: #e6f1fb;
    --label-bottom: #cfe3f5;
    --title-blue: #4b5aa8;
    --brand-purple: #6b2d8f;
    --icon-purple: #7a3b9e;
    --scene-sky: #bcd8f0;
    --scene-soft: #e9f3fb;
    --scene-tub: #f4f8fc;
    --white: #ffffff;
  }
  * { box-sizing: border-box; margin: 0; padding: 0; }
  html, body {
    width: 698px; height: 1200px; overflow: hidden;
    background: var(--page);
  }
  .label {
    position: absolute; left: 40px; top: 60px;
    width: 618px; height: 1080px;
    border-radius: 28px;
    background: linear-gradient(180deg, var(--label-top), var(--label-bottom));
    overflow: hidden;
  }
  .brand {
    position: absolute; left: 50%; top: 34px; transform: translateX(-50%);
    width: 160px; height: 160px; border-radius: 50%;
    background: var(--white);
    display: flex; align-items: center; justify-content: center;
    text-align: center;
  }
  .brand-name {
    font-family: "Jost", sans-serif; font-weight: 600;
    font-size: 22px; letter-spacing: 2px; color: var(--brand-purple);
    text-transform: uppercase; white-space: nowrap;
  }
  .product-title {
    position: absolute; top: 218px; left: 0; right: 0;
    text-align: center;
    font-family: "Fredoka", sans-serif; font-weight: 600;
    font-size: 64px; line-height: 1.08; color: var(--title-blue);
  }
  .claims {
    position: absolute; left: 24px; top: 420px;
    display: flex; flex-direction: column; gap: 18px;
    list-style: none;
  }
  .claims li { width: 56px; height: 56px; }
  .bath-scene {
    position: absolute; left: 100px; top: 395px;
    width: 500px; height: 420px; border-radius: 40px;
    background: radial-gradient(ellipse at 50% 40%, var(--scene-soft), var(--scene-sky) 75%);
  }
  .tub {
    position: absolute; left: 130px; top: 640px;
    width: 440px; height: 150px;
    border-radius: 30px 30px 90px 90px;
    background: var(--scene-tub);
    display: flex; align-items: center; justify-content: center;
  }
  .tub-word {
    font-family: "Fredoka", sans-serif; font-weight: 700;
    font-size: 100px; letter-spacing: 4px; color: var(--brand-purple);
    line-height: 1;
  }
  .endorsement {
    position: absolute; top: 852px; left: 0; right: 0; text-align: center;
    font-family: "Jost", sans-serif; font-weight: 600;
    font-size: 44px; color: var(--brand-purple);
  }
  .net-volume {
    position: absolute; top: 950px; left: 0; right: 0; text-align: center;
    font-family: "Jost", sans-serif; font-weight: 600;
    font-size: 40px; color: var(--brand-purple);
  }
</style>
</head>
<body>
  <main class="label">
    <div class="brand">
      <span class="brand-name">Tot Petal</span>
    </div>

    <h1 class="product-title">Tear-Free<br>Head-to-Toe</h1>

    <div class="bath-scene" role="img" aria-label="Illustration of two children in a bubble bath with a shower head, music notes and a rubber duck"></div>

    <ul class="claims" aria-label="Product claims">
      <li aria-label="Paraben-free">
        <svg viewBox="0 0 56 56" width="56" height="56"><circle cx="28" cy="28" r="26" fill="var(--icon-purple)"/><path d="M28 14 L36 30 A8 8 0 1 1 20 30 Z" fill="none" stroke="#fff" stroke-width="3"/><line x1="14" y1="42" x2="42" y2="14" stroke="#fff" stroke-width="3"/></svg>
      </li>
      <li aria-label="Sulfate-free">
        <svg viewBox="0 0 56 56" width="56" height="56"><circle cx="28" cy="28" r="26" fill="var(--icon-purple)"/><circle cx="22" cy="30" r="6" fill="none" stroke="#fff" stroke-width="3"/><circle cx="34" cy="24" r="5" fill="none" stroke="#fff" stroke-width="3"/><line x1="14" y1="42" x2="42" y2="14" stroke="#fff" stroke-width="3"/></svg>
      </li>
      <li aria-label="Fragrance-free">
        <svg viewBox="0 0 56 56" width="56" height="56"><circle cx="28" cy="28" r="26" fill="var(--icon-purple)"/><rect x="20" y="22" width="16" height="18" rx="3" fill="none" stroke="#fff" stroke-width="3"/><line x1="28" y1="14" x2="28" y2="22" stroke="#fff" stroke-width="3"/><line x1="14" y1="42" x2="42" y2="14" stroke="#fff" stroke-width="3"/></svg>
      </li>
      <li aria-label="Cruelty-free">
        <svg viewBox="0 0 56 56" width="56" height="56"><circle cx="28" cy="28" r="26" fill="var(--icon-purple)"/><path d="M28 40 L17 29 A6 6 0 0 1 28 21 A6 6 0 0 1 39 29 Z" fill="none" stroke="#fff" stroke-width="3" stroke-linejoin="round"/></svg>
      </li>
    </ul>

    <div class="tub"><span class="tub-word">WASH</span></div>

    <p class="endorsement">Pediatrician-developed</p>
    <p class="net-volume">8oz</p>
  </main>
</body>
</html>
```